Box Packaging Design for Yoga Foam Roller

We need a box packaging design for our yoga foam roller.

1. dimensions of box: 31x16x16cm. see template.jpg for design layout & measurements. box example shows an example product & box dimensions.

2. the design style should have an organic, earth-friendly touch to it with natural colors. reference design.jpg shows the exact design style

3. please generally use wavy lines for the edges instead of sharp straight lines.

4. its a 2 color print design: light brown (see reference design) and charcoal dark blue. the "3rd color" is the brown carton base color.

5. schematic drawing.jpg shows a general blueprint for the packaging design and the placement of the elements.

6. please include yoga person from yoga silhouette.jpg and logo from logo.jpg like shown in the schematic drawing

7. please include barcode label.pdf as shown in the schematic drawing

Target Market(s)

We are a young company from Germany selling yoga and sports products in Europe. Our main markets are Germany, UK, France, Italy and Spain. For our latest product, a Yoga Foam Roller.

The target audience are people which are into Yoga, Health, Pilates, Sports and Fitness. The roller can be used to massage tissues and muscles or for a pre-workout warmup program.

Requirements
Must have
• - design style like reference design.jpg
• - dimensions according to template.jpg
• - barcode label
• - "Desigend in Germany"
• - "Made in China"
• - "Velmora Tide" & logo according to project description, "Faszienrolle", "schwarz/blau"
• - two color design (carton background = "3rd color")
Nice to have
• - see project description (wavy lines, yoga person silhouette, ...)
• - "100% Satisfaction Guarantee" label
• - "Money Back Guarantee" label

```html
<!DOCTYPE html>
<html lang="de">
<head>
<meta charset="utf-8">
<title>Velmora Tide – Faszienrolle Verpackung</title>
<link href="https://fonts.googleapis.com/css2?family=Montserrat:wght@300;400;800&display=swap" rel="stylesheet">
<style>
  :root {
    --stage: #4b4b4b;
    --kraft: #c49a6c;
    --kraft-light: #e2bd93;
    --ink: #2c3e57;
    --label-line: #a9825a;
  }
  html, body {
    margin: 0;
    width: 1200px;
    height: 800px;
    overflow: hidden;
    background: var(--stage);
    font-family: "Montserrat", sans-serif;
  }
  .packaging-net {
    position: absolute;
    left: 145px;
    top: 120px;
    display: flex;
    gap: 20px;
    align-items: flex-start;
  }
  .panel { display: block; }
  .brand-name { font-family: "Montserrat", sans-serif; font-weight: 400; font-size: 13px; fill: var(--kraft-light); letter-spacing: 0.5px; }
  .product-title { font-family: "Montserrat", sans-serif; font-weight: 800; font-size: 24px; fill: var(--ink); }
  .product-variant { font-family: "Montserrat", sans-serif; font-weight: 300; font-size: 13px; fill: var(--kraft-light); }
  .tagline { font-family: "Montserrat", sans-serif; font-weight: 400; font-size: 9px; fill: var(--ink); }
  .label-text { font-family: "Montserrat", sans-serif; font-weight: 400; font-size: 7.5px; fill: var(--ink); }
</style>
</head>
<body>
<div class="packaging-net">

  <!-- Top face -->
  <svg class="panel top-face" width="290" height="560" viewBox="0 0 290 560">
    <rect width="290" height="560" fill="var(--kraft)"/>
    <path class="wave-band" d="M0 330 C40 300 70 360 110 340 C150 320 180 360 220 345 C250 335 270 350 290 340 L290 560 L0 560 Z" fill="var(--kraft-light)"/>
    <g class="brand-lockup">
      <circle cx="145" cy="52" r="10" fill="none" stroke="var(--kraft-light)" stroke-width="1.5"/>
      <text class="brand-name" x="145" y="86" text-anchor="middle">Velmora Tide</text>
    </g>
    <text class="product-title" x="145" y="140" text-anchor="middle">Faszienrolle</text>
    <text class="product-variant" x="145" y="164" text-anchor="middle">– Schwarz / Blau –</text>
    <g class="hero-illustration" role="img" aria-label="Light brown lotus flower with a dark blue seated yoga figure silhouette and its reflection">
      <ellipse cx="145" cy="260" rx="95" ry="55" fill="var(--kraft-light)"/>
      <ellipse cx="150" cy="275" rx="35" ry="38" fill="var(--ink)"/>
      <ellipse cx="150" cy="345" rx="30" ry="30" fill="var(--kraft)" opacity="0.8"/>
    </g>
    <text class="tagline" transform="translate(22 400) rotate(90)">Yoga Foam Roller. With 100% LOVE!</text>
  </svg>

  <!-- Side face -->
  <svg class="panel side-face" width="290" height="560" viewBox="0 0 290 560">
    <rect width="290" height="560" fill="var(--kraft)"/>
    <path class="wave-band" d="M0 250 C40 230 80 275 120 258 C160 240 200 280 240 262 C260 254 275 262 290 255 L290 560 L0 560 Z" fill="var(--kraft-light)"/>
    <g class="info-label">
      <rect x="40" y="300" width="210" height="70" rx="14" fill="var(--kraft-light)" stroke="var(--label-line)" stroke-width="1.5"/>
      <text class="label-text" x="145" y="318" text-anchor="middle">Designed in Germany · Made in China</text>
      <text class="label-text" x="145" y="331" text-anchor="middle">Natural foam for muscle and fascia care.</text>
      <text class="label-text" x="145" y="344" text-anchor="middle">Wipe clean with a damp cloth only.</text>
      <text class="label-text" x="145" y="357" text-anchor="middle">Keep away from heat and direct sun.</text>
    </g>
  </svg>

  <!-- End face -->
  <svg class="panel end-face" width="290" height="290" viewBox="0 0 290 290">
    <rect width="290" height="290" fill="var(--kraft-light)"/>
  </svg>

</div>
</body>
</html>
```